Property Management Company Business Cards

Need business cards for a property management company located in Michigan. We manage houses for clients all over the world. Young and modern company, looking for eye catching design. Please work with the attached logo.

Industry/Entity Type

Property Management

Requirements
Must have
• Need lines for address, telephone number, fax number, web site.

Also lines for name, and job title

```html
<!DOCTYPE html>
<html lang="en">
<head>
<meta charset="utf-8">
<title>Harborvale Management – Business Cards</title>
<link href="https://fonts.googleapis.com/css2?family=Open+Sans:wght@400;600;700&display=swap" rel="stylesheet">
<style>
  :root{
    --stage:#ece8e1;
    --blue:#2fb4dc;
    --blue-light:#4cc8e8;
    --blue-deep:#1e8fbd;
    --band:#f2f2f2;
    --ink:#3a3d42;
    --ink-soft:#5b5f66;
    --paper:#ffffff;
  }
  *{box-sizing:border-box;margin:0;padding:0}
  html,body{width:1200px;height:902px;overflow:hidden}
  body{background:var(--stage);font-family:"Open Sans",Arial,sans-serif;color:var(--ink);position:relative}

  .card{position:absolute;width:600px;height:343px;border-radius:22px;overflow:hidden;
        box-shadow:0 10px 24px rgba(0,0,0,.18)}

  /* Front */
  .card--front{left:80px;top:70px;
    background:linear-gradient(160deg,var(--blue-deep) 0%,var(--blue-light) 45%,var(--blue) 70%,var(--blue-deep) 100%)}
  .front-band{position:absolute;left:0;right:0;top:128px;height:104px;background:var(--band);
    border-top:3px solid #3b3f44;border-bottom:3px solid #3b3f44;
    display:flex;align-items:center;padding-left:40px}
  .front-web{position:absolute;right:36px;bottom:30px;font-size:15px;color:#2c3a44;letter-spacing:.3px}

  .brand{display:flex;align-items:center;gap:14px}
  .brand-dot{width:40px;height:40px;border-radius:50%;background:var(--blue);flex:none}
  .brand-name{font-weight:700;font-size:30px;color:var(--ink);letter-spacing:.5px;text-transform:uppercase}

  /* Back */
  .card--back{left:520px;top:490px;background:var(--paper);border-bottom:8px solid var(--blue)}
  .back-brand{position:absolute;left:36px;top:36px}
  .back-brand .brand-name{font-size:26px}
  .back-brand .brand-dot{width:36px;height:36px}
  .back-rule{position:absolute;left:36px;right:36px;top:104px;height:2px;
    background:linear-gradient(90deg,transparent,var(--blue) 50%,transparent)}
  .person{position:absolute;left:36px;top:122px}
  .person-name{font-size:21px;color:var(--ink)}
  .person-title{font-size:13px;color:var(--blue);margin-top:2px}
  .contacts{position:absolute;left:36px;right:30px;top:196px;font-size:14px;color:var(--ink-soft);
    display:grid;grid-template-columns:1fr 1fr;row-gap:9px;column-gap:14px}
  .contacts .address{grid-column:1 / 3}
  .contact{display:flex;align-items:center;gap:8px;white-space:nowrap}
  .contact svg{width:14px;height:14px;flex:none;fill:var(--blue)}
</style>
</head>
<body>

<section class="card card--front" aria-label="Card front">
  <div class="front-band">
    <div class="brand">
      <span class="brand-dot"></span>
      <span class="brand-name">Harborvale Management</span>
    </div>
  </div>
  <p class="front-web">www.harborvalemgmt.com</p>
</section>

<section class="card card--back" aria-label="Card back">
  <div class="brand back-brand">
    <span class="brand-dot"></span>
    <span class="brand-name">Harborvale Management</span>
  </div>
  <div class="back-rule"></div>
  <div class="person">
    <p class="person-name">Daniel Whitmore</p>
    <p class="person-title">General Manager</p>
  </div>
  <div class="contacts">
    <p class="contact address">4820 Lakeview Rd. Suite 210 Grand Rapids, MI 49503</p>
    <p class="contact">
      <svg viewBox="0 0 16 16" aria-hidden="true"><path d="M3.5 1l2.5 3-1.5 1.7c.8 1.9 2.3 3.4 4.3 4.3L10.5 8.5l3 2.5-1.2 2.8C6.5 13.5 2.5 9.5 1 3.2z"/></svg>
      (616) 555-0142
    </p>
    <p class="contact">
      <svg viewBox="0 0 16 16" aria-hidden="true"><path d="M4 1h7v4H4zM2 6h12v7h-2v2H4v-2H2zm3 5v3h6v-3z"/></svg>
      (616) 555-0187
    </p>
    <p class="contact">
      <svg viewBox="0 0 16 16" aria-hidden="true"><path d="M1 3h14v10H1zm1.5 1.2L8 8.5l5.5-4.3z"/></svg>
      hello@harborvalemgmt.com
    </p>
    <p class="contact">
      <svg viewBox="0 0 16 16" aria-hidden="true"><path d="M8 1a7 7 0 100 14A7 7 0 008 1zm0 1.5c.9 0 1.8 2 2 4.5H6c.2-2.5 1.1-4.5 2-4.5zM6 9h4c-.2 2.5-1.1 4.5-2 4.5S6.2 11.5 6 9zM2.6 7h2c.1-1.6.5-3 1-3.9A5.5 5.5 0 002.6 7zm0 2a5.5 5.5 0 003 3.9c-.5-.9-.9-2.3-1-3.9zm8.8 0c-.1 1.6-.5 3-1 3.9A5.5 5.5 0 0013.4 9zm0-2h2a5.5 5.5 0 00-3-3.9c.5.9.9 2.3 1 3.9z"/></svg>
      www.harborvalemgmt.com
    </p>
  </div>
</section>

</body>
</html>
```